Im open to ideas.. I was thinking on my business cards aswell as my logo. a place for my name. email. phone number and abn..

ive attched a file with my business logo. which i dont love the colours.. i was think a dark background with charcoal letters so something along those colour schumes but im open to ideas..

Business

BRL Constructions

```html
<!DOCTYPE html>
<html lang="en">
<head>
<meta charset="UTF-8">
<title>BRL Constructions — Business Card</title>
<link href="https://fonts.googleapis.com/css2?family=Montserrat:wght@400;500;700;800&display=swap" rel="stylesheet">
<style>
  :root {
    --page: #e9e6e1;
    --card-black: #0b0b0c;
    --card-charcoal: #1c1c1e;
    --accent-red: #e3202a;
    --edge-white: #eeeeee;
    --text-white: #f2f2f2;
    --text-grey: #bdbdbd;
  }
  * { margin: 0; padding: 0; box-sizing: border-box; }
  html, body {
    width: 1200px; height: 1022px; overflow: hidden;
    background: var(--page);
    font-family: "Montserrat", Arial, sans-serif;
  }
  .card {
    position: absolute; left: 100px; top: 221px;
    width: 1000px; height: 580px;
    border-radius: 22px; overflow: hidden;
    background: linear-gradient(160deg, var(--card-charcoal) 0%, var(--card-black) 55%);
    box-shadow: 0 18px 40px rgba(0,0,0,.25);
  }
  .edge-band { position: absolute; right: 0; top: 0; width: 44px; height: 100%; }
  .edge-band__red { height: 72%; background: var(--accent-red); }
  .edge-band__white { height: 28%; background: var(--edge-white); }
  .name-tab {
    position: absolute; right: 44px; top: 0; width: 44px; height: 34px;
    background: var(--edge-white); border-bottom: 10px solid var(--accent-red);
  }
  .brand {
    position: absolute; left: 70px; top: 210px;
    display: flex; align-items: center; gap: 18px;
  }
  .brand__mark { width: 26px; height: 26px; background: var(--accent-red); }
  .brand__name {
    color: var(--text-white); font-weight: 800; font-size: 40px; letter-spacing: 1px;
    text-transform: uppercase; line-height: 1;
  }
  .holder {
    position: absolute; right: 118px; top: 70px; text-align: right;
  }
  .holder__name {
    color: var(--accent-red); font-weight: 700; font-size: 34px;
    letter-spacing: 2px; text-transform: uppercase;
  }
  .holder__role { color: var(--text-white); font-size: 22px; margin-top: 6px; }
  .divider {
    position: absolute; left: 400px; right: 118px; top: 175px;
    height: 2px; background: var(--accent-red);
  }
  .contacts {
    position: absolute; left: 400px; top: 380px; list-style: none;
  }
  .contacts li {
    display: flex; align-items: center; gap: 14px;
    color: var(--text-white); font-size: 23px; line-height: 36px;
  }
  .contacts svg { width: 18px; height: 18px; flex: none; }
  .abn {
    position: absolute; right: 90px; top: 238px;
    color: var(--text-white); font-size: 24px; letter-spacing: 1px;
  }
  .abn__label { color: var(--accent-red); font-weight: 700; }
</style>
</head>
<body>
  <div class="card">
    <div class="edge-band">
      <div class="edge-band__red"></div>
      <div class="edge-band__white"></div>
    </div>
    <div class="name-tab"></div>

    <div class="brand">
      <span class="brand__mark"></span>
      <span class="brand__name">BRL Constructions</span>
    </div>

    <div class="holder">
      <div class="holder__name">Marcus Hale</div>
      <div class="holder__role">Director</div>
    </div>
    <div class="divider"></div>

    <div class="abn"><span class="abn__label">ABN</span>: 41 208 615 307</div>

    <ul class="contacts">
      <li>
        <svg viewBox="0 0 24 24"><path fill="#e3202a" d="M6.6 10.8a15 15 0 0 0 6.6 6.6l2.2-2.2a1 1 0 0 1 1-.25 11.4 11.4 0 0 0 3.6.57 1 1 0 0 1 1 1V20a1 1 0 0 1-1 1A17 17 0 0 1 3 4a1 1 0 0 1 1-1h3.5a1 1 0 0 1 1 1c0 1.25.2 2.45.57 3.57a1 1 0 0 1-.25 1z"/></svg>
        +330 2460-1184
      </li>
      <li>
        <svg viewBox="0 0 24 24"><rect x="2" y="5" width="20" height="14" rx="1" fill="none" stroke="#e3202a" stroke-width="2.4"/><path d="M3 6l9 7 9-7" fill="none" stroke="#e3202a" stroke-width="2.4"/></svg>
        info@brlconstructions.com
      </li>
      <li>
        <svg viewBox="0 0 24 24"><circle cx="12" cy="12" r="10" fill="#e3202a"/><path d="M2 12h20M12 2c3 3 3 17 0 20M12 2c-3 3-3 17 0 20" fill="none" stroke="#0b0b0c" stroke-width="1.5"/></svg>
        www.brlconstructions.com
      </li>
    </ul>
  </div>
</body>
</html>
```